Sip. Stroll. Flourish. Book Cover

I would like a book cover for the print edition book I am self publishing. My cover will require front, back, and spine design. I have provided a template to assist with sizing and spacing.

My book is named "Sip. Stroll. Flourish. A Simple Diet, Drive to Stretch, and Outlook Manual Building Traction Along Better Vigor and Balance" by Gregory Talbrecht RD, CPT. I use the concept of waves as an analogy for forward progress in life and would like that reflected in the cover design. I would like the color scheme to be blacks, whites, grey, and various shades of blue. I have provided a style guide for reference. Please include my logo on the front, spine, and back of the design. Please include an about the author, book summary, and my picture on the back. I have provided the wording below.

About the Author: Gregory Talbrecht is a Registered Dietitian and Certified Personal Trainer from Cleveland, OH. He graduated from the Verdant Plains University and currently works as a health coach in the healthcare industry. His passions are fitness, nutrition, science, and motivation. He has extensive knowledge and experience in wellness, healthcare, and disease treatment and disease. Gregory has worked with hundreds of people through counseling, consulting, and coaching in an effort to make a difference in their long-term health. In his spare time, he enjoys exercising, watching movies, and trying out new foods.

Book Summary: Believe in you. Trust in You. Sip. Stroll. Flourish. is a book committed to you. Behavior change and improved health can be challenging. You must feel empowered to make decisions and changes create momentum in the right direction. But, you may not always have the knowledge to do that. This book provides you with practical and fun tools and tips to improve your nutrition, motivation to move, and mindset. You are awesome. You are beautiful. You have the power to control your destiny and future. All you have to do is Sip, Stroll, and Flourish!

Please use a modern/ futuristic font style for the title. I have also provided some draft book covers for inspiration/ direction. Thank you!

Colors

Designer to choose only greyscale colors for use in the design.

Requirements
Must have
• Color scheme, about author, profile picture, and book summary on back, wave themed graphics

```html
<!DOCTYPE html>
<html lang="en">
<head>
<meta charset="utf-8">
<title>Sip. Stroll. Flourish. — Book Cover</title>
<link rel="stylesheet" href="https://fonts.googleapis.com/css2?family=Arimo:wght@400;500&display=swap">
<style>
  :root {
    --page-bg: #ececec;
    --cover-top: #8c8c8c;
    --cover-mid: #3a3a3a;
    --cover-bottom: #161616;
    --band-slate: #3f4956;
    --band-text: #c9d3dc;
    --band-mark: #5f86a8;
    --text-light: #f2f2f2;
    --text-soft: #dcdcdc;
  }
  html, body {
    margin: 0;
    width: 1200px;
    height: 1200px;
    overflow: hidden;
    background: var(--page-bg);
    font-family: "Arimo", Arial, sans-serif;
  }
  .book-cover {
    position: absolute;
    left: 247px;
    top: 50px;
    width: 706px;
    height: 1100px;
    overflow: hidden;
    background: linear-gradient(180deg, var(--cover-top) 0%, #6f6f6f 12%, var(--cover-mid) 55%, #222 75%, var(--cover-bottom) 100%);
  }
  .wave-art {
    position: absolute;
    left: 0;
    top: 150px;
    width: 100%;
    height: 560px;
    background:
      radial-gradient(ellipse 38% 30% at 78% 22%, #f4f4f4 0%, #bdbdbd 35%, rgba(120,120,120,0) 75%),
      linear-gradient(160deg, #9a9a9a 0%, #555 35%, #2e2e2e 60%, #3a3a3a 80%, rgba(34,34,34,0) 100%);
  }
  .brand-band {
    position: absolute;
    left: 142px;
    top: 0;
    width: 492px;
    height: 172px;
    background: var(--band-slate);
    display: flex;
    align-items: center;
    justify-content: center;
    gap: 18px;
  }
  .brand-mark {
    width: 34px;
    height: 34px;
    background: var(--band-mark);
  }
  .brand-name {
    font-size: 34px;
    font-weight: 500;
    color: var(--band-text);
    letter-spacing: 0.5px;
  }
  .cover-text {
    position: absolute;
    left: 0;
    width: 100%;
    text-align: center;
    color: var(--text-light);
  }
  .subtitle {
    top: 712px;
    font-size: 20px;
    color: var(--text-soft);
  }
  .title {
    top: 748px;
    margin: 0;
    font-size: 54px;
    font-weight: 400;
    line-height: 60px;
    padding: 0 40px;
    box-sizing: border-box;
  }
  .author {
    top: 1004px;
    font-size: 24px;
  }
</style>
</head>
<body>
  <main class="book-cover">
    <div class="wave-art" role="img" aria-label="Black and white photograph of a cresting ocean wave with sunlight breaking through the spray"></div>
    <div class="brand-band">
      <span class="brand-mark"></span>
      <span class="brand-name">Sip. Stroll. Flourish.</span>
    </div>
    <div class="cover-text subtitle">A Simple Diet, Drive to Stretch, and Outlook Manual</div>
    <h1 class="cover-text title">Building Traction Along Better Vigor and Balance</h1>
    <div class="cover-text author">Gregory Talbrecht RD, CPT</div>
  </main>
</body>
</html>
```